Modern looking signage for dental office.

Exterior signage for passing cars
Target Market(s)
Cars passing by
Font styles to use
Sans Serif
Colors
3276b5
Requirements
Must have
- Logo
- OPEN ON SUTURDAY AND SUNDAY
- NIGHT CLINIC AVAILABLE
- PLEASE USE THE FONT TYPE IN FILE 4 UPLOADED BELOW.
- (482) 730-2964
- Modern looking

```html
<!DOCTYPE html>
<html lang="en">
<head>
<meta charset="utf-8">
<title>Crest Dental – Weekend &amp; Night Clinic Sign</title>
<link rel="stylesheet" href="https://fonts.googleapis.com/css2?family=Open+Sans:wght@300;400;700;800&family=Josefin+Sans:wght@300&family=Encode+Sans+Condensed:wght@400&display=swap">
<style>
  :root {
    --sign-white: #f7f7f7;
    --ink-dark: #333333;
    --logo-gray: #555555;
    --teal-deep: #268aa1;
    --teal-mid: #5aa8bc;
    --teal-light: #a4d0dc;
    --text-white: #ffffff;
  }
  html, body {
    margin: 0;
    padding: 0;
    width: 1200px;
    height: 1200px;
    overflow: hidden;
    background: var(--sign-white);
  }
  .sign {
    display: block;
    width: 1200px;
    height: 1200px;
  }
  .brand-name {
    font-family: "Josefin Sans", sans-serif;
    font-weight: 300;
    fill: var(--logo-gray);
  }
  .brand-mark { fill: none; stroke: var(--logo-gray); stroke-width: 3; }
  .brand-tagline {
    font-family: "Encode Sans Condensed", sans-serif;
    font-weight: 400;
    fill: var(--logo-gray);
  }
  .headline, .days, .hours, .phone, .website { font-family: "Open Sans", sans-serif; }
  .headline { font-weight: 800; fill: var(--text-white); }
  .days { font-weight: 800; fill: var(--text-white); }
  .days .light { font-weight: 300; }
  .hours { font-weight: 400; fill: var(--text-white); }
  .hours .strong { font-weight: 700; }
  .phone { font-weight: 800; fill: var(--ink-dark); }
  .website { font-weight: 400; fill: var(--ink-dark); }
  .website .strong { font-weight: 700; }
  .contact-panel { fill: #ffffff; }
  .footer-strip { fill: var(--teal-deep); }
</style>
</head>
<body>
<svg class="sign" viewBox="0 0 1200 1200" xmlns="http://www.w3.org/2000/svg">
  <defs>
    <linearGradient id="tealFill" x1="0" y1="0" x2="0" y2="1">
      <stop offset="0" stop-color="var(--teal-light)"/>
      <stop offset="0.35" stop-color="var(--teal-mid)"/>
      <stop offset="0.5" stop-color="var(--teal-deep)"/>
      <stop offset="1" stop-color="var(--teal-deep)"/>
    </linearGradient>
  </defs>

  <rect width="1200" height="1200" fill="var(--sign-white)"/>

  <!-- Brand -->
  <g class="brand">
    <circle class="brand-mark" cx="223" cy="166" r="103"/>
    <text class="brand-name" x="347" y="209" font-size="126" textLength="733" lengthAdjust="spacingAndGlyphs">CREST DENTAL</text>
    <text class="brand-tagline" x="420" y="276" font-size="50" textLength="564" lengthAdjust="spacingAndGlyphs">MODERN GENERAL DENTISTRY</text>
  </g>

  <!-- Illustration area -->
  <rect class="illustration-area" x="82" y="300" width="1118" height="900" fill="url(#tealFill)" role="img" aria-label="Stylised tooth-shaped wave illustration in dark gray and teal"/>

  <!-- Contact panel -->
  <rect class="contact-panel" x="82" y="912" width="1118" height="213"/>
  <rect class="footer-strip" x="82" y="1125" width="1118" height="75"/>

  <!-- Message -->
  <text class="headline" x="277" y="647" font-size="178" textLength="810" lengthAdjust="spacingAndGlyphs">OPEN ON</text>
  <text class="days" x="277" y="727" font-size="72" textLength="810" lengthAdjust="spacingAndGlyphs">SATURDAY <tspan class="light">AND</tspan> SUNDAY</text>
  <text class="hours" x="277" y="839" font-size="62" textLength="810" lengthAdjust="spacingAndGlyphs">Night clinic from <tspan class="strong">5pm</tspan> to <tspan class="strong">10pm</tspan></text>

  <!-- Contact -->
  <text class="phone" x="300" y="1039" font-size="124" textLength="767" lengthAdjust="spacingAndGlyphs">482 730 2964</text>
  <text class="website" x="300" y="1089" font-size="30" textLength="767" lengthAdjust="spacing">www.<tspan class="strong">CrestDentalClinic</tspan>.com</text>
</svg>
</body>
</html>
```